Corporate Intelligence Agency seeks redesign *

Brightfen Advisory is a business intelligence firm made up of former special operations and intelligence professionals. Our vibe is quiet professionals that get the job done by whatever means necessary.
Our aesthetic is clean, sleek, and monochromatic. We prefer the texture contrasts over colors. Slick white or black, playing up textures, and bold block lettering, and simplicity are what we are looking for in a design.

The logo would preferably pay homage to our military/special operations roots, and the culture of changing for the better (alchemy) that we embody all while remaining simple.

Target Market(s)

C-Level executives with a taste for the simple over the extravagant, and cut right to the chase

Industry/Entity Type

Management Solution

Contact Information for Business Card

Back is matte black with a glossy black logo to contrast. The front has the logo, with space on the bottom left for name and contact

Logo Text

Brightfen Adv.

Logo styles of interest
Abstract Logo
Wordmark Logo
Lettermark Logo
Font styles to use
Serif
Sans Serif
Script

Requirements
Must have
• Monochromatic, play on texture within card (the card ought to be memorable to hold), solid/clean lettering. Logo should be simple and sleek.
Nice to have
• If the logo can tie alchemy and intelligence/spy genre. 3d textures
Should not have
• Nothing overtly military. No colors outside of the monochromatic spectrum

```html
<!DOCTYPE html>
<html lang="en">
<head>
<meta charset="utf-8">
<title>Brightfen Advisory — Business Card</title>
<link rel="stylesheet" href="https://fonts.googleapis.com/css2?family=Jost:wght@300;400&family=Oswald:wght@300;400;500&display=swap">
<style>
  :root {
    --page: #ffffff;
    --card-black: #000000;
    --card-wedge: #2b2b2d;
    --ink-white: #ffffff;
    --ink-grey: #8a8a8a;
    --ink-grey-dim: #6e6e6e;
  }
  html, body {
    margin: 0;
    padding: 0;
    width: 1200px;
    height: 1000px;
    overflow: hidden;
    background: var(--page);
  }
  .canvas {
    position: relative;
    width: 1200px;
    height: 1000px;
  }
  .card {
    position: absolute;
    left: 220px;
    top: 290px;
    width: 734px;
    height: 420px;
    background: var(--card-black);
    overflow: hidden;
  }
  .card-wedges {
    position: absolute;
    inset: 0;
    width: 100%;
    height: 100%;
  }
  .card-wedges polygon { fill: var(--card-wedge); }
  .card-text {
    position: absolute;
    left: 0;
    width: 100%;
    margin: 0;
    text-align: center;
    white-space: nowrap;
    line-height: 1;
    /* greyscale antialiasing keeps thin type strictly monochrome */
    -webkit-font-smoothing: antialiased;
    -moz-osx-font-smoothing: grayscale;
    will-change: transform;
    transform: translateZ(0);
  }
  .holder-name {
    top: 58px;
    font-family: "Jost", sans-serif;
    font-weight: 400;
    font-size: 20px;
    letter-spacing: 0.25em;
    padding-left: 0.25em;
    color: var(--ink-white);
  }
  .wordmark {
    top: 182px;
    font-family: "Jost", sans-serif;
    font-weight: 300;
    font-size: 56px;
    letter-spacing: 0.2em;
    padding-left: 0.2em;
    color: var(--ink-white);
  }
  .wordmark-sub {
    top: 249px;
    font-family: "Oswald", sans-serif;
    font-weight: 500;
    font-size: 13px;
    letter-spacing: 1.1em;
    padding-left: 1.1em;
    color: var(--ink-grey-dim);
  }
  .holder-title {
    top: 325px;
    font-family: "Oswald", sans-serif;
    font-weight: 400;
    font-size: 19px;
    letter-spacing: 0.4em;
    padding-left: 0.4em;
    color: var(--ink-grey);
  }
  .holder-info {
    top: 361px;
    font-family: "Oswald", sans-serif;
    font-weight: 300;
    font-size: 15px;
    letter-spacing: 0.45em;
    padding-left: 0.45em;
    color: var(--ink-grey);
  }
</style>
</head>
<body>
  <main class="canvas">
    <section class="card">
      <svg class="card-wedges" viewBox="0 0 734 420" preserveAspectRatio="none" aria-hidden="true">
        <polygon points="0,0 0,420 367,210"/>
        <polygon points="734,0 734,420 367,210"/>
      </svg>
      <p class="card-text holder-name">JOHN DOE</p>
      <p class="card-text wordmark">BRIGHTFEN</p>
      <p class="card-text wordmark-sub">ADVISORY</p>
      <p class="card-text holder-title">TITLE</p>
      <p class="card-text holder-info">OTHER INFORMATION</p>
    </section>
  </main>
</body>
</html>
```